KVO Real Estate

I am looking for a fresh idea for our business cards. Would like to incorporate our realtors photos as well as company logo and contact info. I will upload our logo but would also be interested in changing the REAL ESTATE text at the bottom of the logo to something fresher as well. I have also include the card we currently use.

Requirements. Agent name, title, contact info needs to be easily updated. Interested in designs for front and back. Will need the final layered file with individual layers for all text and photo elements.

Reason: Down to a few finalists. Will be making a decision shortly.

```html
<!DOCTYPE html>
<html lang="en">
<head>
<meta charset="utf-8">
<title>KVO Real Estate – Business Card</title>
<link href="https://fonts.googleapis.com/css2?family=Open+Sans:wght@400;600&display=swap" rel="stylesheet">
<style>
  :root {
    --stage: #2b5bd6;
    --card: #f7f8fb;
    --navy: #1d2f7a;
    --edge: #26409a;
    --ink: #3c4250;
    --muted: #5a6070;
    --accent: #e0661e;
    --photo-a: #8c9aa8;
    --photo-b: #c9a48c;
  }
  * { box-sizing: border-box; margin: 0; padding: 0; }
  html, body { width: 1200px; height: 1000px; overflow: hidden; }
  body {
    background: var(--stage);
    font-family: "Open Sans", Arial, sans-serif;
    display: flex; align-items: center; justify-content: center;
  }
  .card {
    position: relative;
    width: 1000px; height: 572px;
    background: var(--card);
    box-shadow: 0 20px 50px rgba(0, 0, 30, .35);
    overflow: hidden;
  }
  .card__edge {
    position: absolute; left: 0; top: 0; bottom: 0; width: 22px;
    background: var(--edge);
  }
  .agent-photo {
    position: absolute; top: 34px; right: 56px;
    width: 220px; height: 150px;
    background: linear-gradient(135deg, var(--photo-a), var(--photo-b));
  }
  .agent {
    position: absolute; top: 196px; right: 56px; text-align: right;
  }
  .agent__name { color: var(--navy); font-size: 40px; font-weight: 600; line-height: 1.15; }
  .agent__title { color: var(--muted); font-size: 26px; line-height: 1.2; }
  .credentials {
    position: absolute; top: 330px; right: 56px; text-align: right;
    font-size: 17px; line-height: 1.6;
  }
  .credentials__web { color: var(--navy); font-weight: 600; }
  .credentials__license { color: var(--ink); }
  .brand {
    position: absolute; top: 176px; left: 78px;
    display: flex; align-items: center; gap: 14px;
  }
  .brand__dot { width: 40px; height: 40px; border-radius: 50%; background: var(--accent); }
  .brand__name { color: var(--navy); font-size: 30px; font-weight: 600; }
  .contact {
    position: absolute; top: 268px; left: 100px; list-style: none;
    color: var(--ink); font-size: 22px; line-height: 1.4;
  }
  .contact__item { display: flex; gap: 20px; margin-bottom: 22px; }
  .contact__icon { width: 22px; height: 22px; margin-top: 5px; flex: none; fill: none; stroke: var(--navy); stroke-width: 2; }
</style>
</head>
<body>
  <article class="card">
    <div class="card__edge"></div>

    <div class="agent-photo" role="img" aria-label="Portrait photo of the realtor"></div>
    <div class="agent">
      <div class="agent__name">Dana Whitfield</div>
      <div class="agent__title">Realtor</div>
    </div>
    <div class="credentials">
      <div class="credentials__web">www.kvohomesgroup.com</div>
      <div class="credentials__license">CalBRE: 01483920 / NMLS: 315608</div>
    </div>

    <div class="brand">
      <span class="brand__dot"></span>
      <span class="brand__name">KVO Real Estate</span>
    </div>

    <ul class="contact">
      <li class="contact__item">
        <svg class="contact__icon" viewBox="0 0 24 24"><path d="M6 3l3 1 1 5-2 1.5a12 12 0 0 0 5.5 5.5L15 14l5 1 1 3-2 3C10 20 4 14 3 5z"/></svg>
        <div>Office: (555) 410-2280 x214<br>Direct: (555) 318-7764<br>Fax: (555) 410-2291</div>
      </li>
      <li class="contact__item">
        <svg class="contact__icon" viewBox="0 0 24 24"><path d="M3 11l9-8 9 8M5 9.5V21h14V9.5M10 21v-6h4v6"/></svg>
        <div>2840 Harbor Way, Ste 12<br>Bayview, CA 95012</div>
      </li>
      <li class="contact__item">
        <svg class="contact__icon" viewBox="0 0 24 24"><rect x="3" y="5" width="18" height="14"/><path d="M3 5l9 8 9-8"/></svg>
        <div>dana@kvorealestate.com</div>
      </li>
    </ul>
  </article>
</body>
</html>
```